plivant-compatible banner ad set and associated landing page design

This is the message that the banner should communicate:
"Get Paid to Save the Planet - Solar Pays You Up to $750+ Every Year for Use of Your Roof"
BANNER SIZE:  300x250 would be great. (After choosing the winner, we will pay additional money to create new versions indifferent sizes as a follow-on work.)
BANNER FORMAT:  Could be an animated GIF, static JPG HTML 5, video, your call.
As for design guidelines for the ad and landing page, follow design guidance at: http://qr-tx41.vendolix.com/rs/clickharvo/images/10%20blunders%20layout_final%20(1).pdf
The banner ad will be used on the Plivant Ad network and should have a call to action to get the user to click to the landing page. The call to action can be two buttons within the banner ad:
"I Care About Planet Earth"
"Don't Care"
Clicking anywhere on the banner ad will drive traffic to the landing page.
On the landing page, we want a design that we can implement in sitelumora.com to capture the following information:
- Street Number and Street Name of My Home
- My Zip Code
- Name of My Electric Utility
- My Typical Monthly Electric Bill Amount is:
- How Much I'd Like to Earn From Solar Per-Year?
After the user fills out the above, the following questions drop down:
First Name
Last Name
Email Address
Phone Number
At the end of the data entry portion of the landing page, there should be a "call to action" button.
LANDING PAGE FORMAT:  Photoshop or jpg format or html5 format would be great.

Updates
Target Market(s)
home owners
Industry/Entity Type
Home Improvement
Requirements
Nice to have
- Follow design guidance at: http://qr-tx41.vendolix.com/rs/clickharvo/images/10%20blunders%20layout_final%20(1).pdf

```html
<!DOCTYPE html>
<html lang="en">
<head>
<meta charset="utf-8">
<title>Solar Banner Set</title>
<link rel="stylesheet" href="https://fonts.googleapis.com/css2?family=Montserrat:wght@500;600;700&display=swap">
<style>
  :root {
    --page-bg: #0b0b0b;
    --banner-green: #2e5716;
    --banner-green-dark: #1f3f0e;
    --banner-green-light: #3b6a1f;
    --banner-border: #d9d9d9;
    --text-white: #ffffff;
    --accent-yellow: #fdd423;
    --care-border: #8fb82f;
    --decline-red: #c2330a;
    --decline-border: #e8a88c;
    --text-dark: #1b1b1b;
  }
  html, body {
    margin: 0;
    padding: 0;
    width: 1200px;
    height: 900px;
    overflow: hidden;
    background: var(--page-bg);
    font-family: "Montserrat", Arial, sans-serif;
  }
  .canvas {
    position: relative;
    width: 1200px;
    height: 900px;
  }
  .banner {
    position: absolute;
    top: 261px;
    width: 450px;
    height: 375px;
    border: 1px solid var(--banner-border);
    overflow: hidden;
    color: var(--text-white);
    text-align: center;
  }
  .banner--question { left: 111px; }
  .banner--offer { left: 638px; }
  .banner__backdrop {
    position: absolute;
    inset: 0;
    background:
      radial-gradient(circle at 50% 48%, var(--banner-green-light) 0%, var(--banner-green) 45%, var(--banner-green-dark) 100%);
  }
  .banner__content {
    position: absolute;
    inset: 0;
  }
  .question {
    position: absolute;
    top: 40px;
    left: 0;
    right: 0;
    margin: 0;
    font-size: 35px;
    line-height: 48px;
    font-weight: 600;
  }
  .choice {
    position: absolute;
    left: 84px;
    width: 281px;
    box-sizing: border-box;
    border-radius: 8px;
    display: flex;
    align-items: center;
    justify-content: center;
    font-size: 33px;
    font-weight: 500;
  }
  .choice--care {
    top: 174px;
    height: 65px;
    background: var(--accent-yellow);
    border: 2px solid var(--care-border);
    color: var(--text-dark);
  }
  .choice--decline {
    top: 262px;
    height: 70px;
    background: var(--decline-red);
    border: 2px solid var(--decline-border);
    color: var(--text-white);
  }
  .offer-title {
    position: absolute;
    top: 67px;
    left: 0;
    right: 0;
    margin: 0;
    font-size: 46px;
    line-height: 59px;
    font-weight: 600;
  }
  .offer-title__accent {
    display: block;
    color: var(--accent-yellow);
  }
  .offer-detail {
    position: absolute;
    top: 198px;
    left: 0;
    right: 0;
    margin: 0;
    font-size: 22px;
    line-height: 36px;
    font-weight: 600;
  }
</style>
</head>
<body>
<main class="canvas">
  <section class="banner banner--question">
    <div class="banner__backdrop" role="img" aria-label="Faint world globe with radiating sun rays on a green background"></div>
    <div class="banner__content">
      <h2 class="question">Do You Care<br>About Planet Earth?</h2>
      <div class="choice choice--care">I Care</div>
      <div class="choice choice--decline">I Don’t Care</div>
    </div>
  </section>

  <section class="banner banner--offer">
    <div class="banner__backdrop" role="img" aria-label="Faint world globe with radiating sun rays on a green background"></div>
    <div class="banner__content">
      <h2 class="offer-title">Get Paid to<span class="offer-title__accent">Save the Planet</span></h2>
      <p class="offer-detail">Solar Pays You Up to<br>$750+ Every Year for<br>Use of Your Roof</p>
    </div>
  </section>
</main>
</body>
</html>
```